Freeze Dried Raw Dog Food Label

Create a label for a Freeze Dried Raw dog and cat food line.
There are four flavors (beef, bison, fish and chicken).
4 x 8" Label FRONT AND BACK
Please see website www.tolvernfeeds.com for our other product labels that this will need to stand next to.
Please use this color codes for the different flavors:
Chicken: #d5c55c
Beef: 469b9f
Bison: #275e6d
Fish: #a07980
The only other colors that should be used are Black, White, gray scale, and the shiny metallic gold as seen on our website: www.tolvernfeeds.com
There will have 8 Variations:
Beef for dogs
Beef for Cats
Chicken for dogs
Chicken for cats
Bison for dogs
Bison for cats
Fish for dogs
Fish for cats.
There will be (2) 4X8 inch labels for each variation (a front side and a back side)
The Nutritional Information of the 4 flavors, is as follows:
BEEF
Ingredients
Beef, Beef Kidneys, Beef Hearts, Beef Liver, Whole Egg, Flaxseed, Organic Sweet Potato, Kelp, Organic Carrots, Organic Apples, Organic Blueberries, Cod Liver Oil, Pumpkin Seeds, Organic Spinach, Chicory Root, Organic Cranberries, Ginger, Mixed Tocopherols, Inulin, Dried Enterococcus faecium, Fermentation Product, Dried Lactobacillus acidophilus fermentation product
Calorie Content
Kcal/Cup 182
Guaranteed Analysis
Crude Protein – 38% (min)
Crude Fat – 36% (min)
Crude Fiber – 4% (max)
Moisture – 5% (max)
CHICKEN
Ingredients
Chicken, Chicken Liver, Chicken Hearts, Whole Egg, Flaxseed, Organic Sweet Potato, Kelp, Organic Carrots, Organic Apples, Organic Blueberries, Cod Liver Oil, Pumpkin Seeds, Organic Spinach, Chicory Root, Organic Cranberries, Ginger, Mixed Tocopherols, Inulin, Dried Enterococcus faecium, Fermentation Product, Dried Lactobacillus acidophilus fermentation product.
Calorie Content
Kcal/Cup 185
Guaranteed Analysis
Crude Protein – 45% (min)
Crude Fat – 34% (min)
Crude Fiber – 4% (max)
Moisture – 5% (max)
BISON:
Ingredients
Bison, Bison kidneys, Bison Livers, Whole Egg, Flaxseed, Organic Sweet Potato, Kelp, Organic Carrots, Organic Apples, Organic Blueberries, Cod Liver Oil, Pumpkin Seeds, Organic Spinach, Chicory Root, Organic Cranberries, Ginger, Mixed Tocopherols, Inulin, Dried Enterococcus faecium, Fermentation Product, Dried Lactobacillus acidophilus fermentation product.
Calorie Content
Kcal/Cup 186
Guaranteed Analysis
Crude Protein – 32% (min)
Crude Fat – 38% (min)
Crude Fiber – 5% (max)
Moisture – 5% (max)
FISH
Ingredients
Tuna, Salmon, Pollock, Whole Egg, Flaxseed, Organic Sweet Potato, Kelp, Organic Carrots, Organic Apples, Organic Blueberries, Cod Liver Oil, Pumpkin Seeds, Organic Spinach, Chicory Root, Organic Cranberries, Ginger, Mixed Tocopherols, Inulin, Dried Enterococcus faecium, Fermentation Product, Dried Lactobacillus acidophilus fermentation product.
Calorie Content
Kcal/Cup 455, Kcal/oz 114
Guaranteed Analysis
Crude Protein – 40% (min)
Crude Fat – 37% (min)
Crude Fiber – 4% (max)
Moisture – 5% (max)
THINGS TO ADD
Feeding Guidelines: Insert a QR CODE

```html
<!DOCTYPE html>
<html lang="en">
<head>
<meta charset="utf-8">
<title>Tolvern Feeds – Freeze Dried Raw Labels</title>
<link href="https://fonts.googleapis.com/css2?family=Michroma&family=Roboto:wght@300&display=swap" rel="stylesheet">
<style>
  :root {
    --bg: #ffffff;
    --label: #ffffff;
    --ink: #111111;
    --gray-soft: #d9d9d9;
    --gray-mid: #8a8a8a;
    --chicken: #d5c55c;
    --beef: #469b9f;
    --gold-dark: #b07a1e;
    --gold-light: #f3dc9a;
  }
  * { margin: 0; padding: 0; box-sizing: border-box; }
  html, body { width: 1200px; height: 1200px; overflow: hidden; background: var(--bg); }
  .canvas { position: relative; width: 1200px; height: 1200px; }
  .label {
    position: absolute; top: 290px; width: 360px; height: 620px;
    background: var(--label); box-shadow: 0 0 0 1px #eeeeee;
    overflow: hidden;
  }
  .label--dog { left: 180px; }
  .label--cat { left: 660px; }
  .label--dog { --flavor: var(--chicken); }
  .label--cat { --flavor: var(--beef); }

  .brand {
    position: absolute; top: 170px; left: 110px; right: 30px;
    text-align: center; font-family: "Michroma", sans-serif;
    color: var(--ink);
  }
  .brand__name { font-size: 26px; line-height: 1.1; letter-spacing: 1px; }
  .brand__tier { font-size: 11px; letter-spacing: 6px; margin-top: 6px; }
  .brand__rule { height: 2px; margin: 6px 20px 0; background: linear-gradient(90deg, var(--gold-dark), var(--gold-light), var(--gold-dark)); }

  .portrait {
    position: absolute; top: 270px; left: 10px; width: 150px; height: 170px;
    border-radius: 45% 45% 35% 40%;
    background: radial-gradient(ellipse at 55% 45%, #f4f4f4 0%, #c9c9c9 60%, #ffffff 100%);
  }
  .swoosh { position: absolute; left: 0; top: 0; width: 360px; height: 620px; }

  .flavor-icon {
    position: absolute; top: 410px; left: 225px; width: 80px; height: 60px;
    background: var(--flavor); border-radius: 18px 24px 10px 10px;
  }
  .flavor-name {
    position: absolute; top: 490px; right: 20px;
    font-family: "Michroma", sans-serif; font-size: 17px; color: var(--flavor);
  }
  .title {
    position: absolute; left: 20px; top: 520px; color: var(--flavor);
  }
  .title__freeze { font-family: "Michroma", sans-serif; font-size: 22px; line-height: 1.2; }
  .title__raw { font-family: "Roboto", sans-serif; font-weight: 300; font-size: 38px; line-height: 1; letter-spacing: 1px; }
  .species {
    position: absolute; right: 14px; top: 562px;
    font-family: "Michroma", sans-serif; font-size: 11px; line-height: 1; color: var(--ink);
    text-align: right;
  }
</style>
</head>
<body>
<main class="canvas">

  <section class="label label--dog">
    <div class="portrait" role="img" aria-label="Pencil-sketch portrait of a dog"></div>
    <svg class="swoosh" viewBox="0 0 360 620" aria-hidden="true">
      <defs>
        <linearGradient id="gold-dog" x1="0" y1="1" x2="1" y2="0">
          <stop offset="0" stop-color="#b07a1e"/>
          <stop offset="0.5" stop-color="#f3dc9a"/>
          <stop offset="1" stop-color="#b07a1e"/>
        </linearGradient>
      </defs>
      <path d="M0 505 C 150 460, 280 380, 360 210 L 360 216 C 282 386, 152 470, 0 512 Z" fill="url(#gold-dog)"/>
    </svg>
    <div class="brand">
      <div class="brand__name">Tolvern</div>
      <div class="brand__tier">FEEDS</div>
      <div class="brand__rule"></div>
    </div>
    <div class="flavor-icon" role="img" aria-label="Chicken silhouette"></div>
    <div class="flavor-name">CHICKEN</div>
    <div class="title">
      <div class="title__freeze">Freeze</div>
      <div class="title__raw">DRIED RAW</div>
    </div>
    <div class="species">DOG<br>FOOD</div>
  </section>

  <section class="label label--cat">
    <div class="portrait" role="img" aria-label="Pencil-sketch portrait of a tabby cat"></div>
    <svg class="swoosh" viewBox="0 0 360 620" aria-hidden="true">
      <defs>
        <linearGradient id="gold-cat" x1="0" y1="1" x2="1" y2="0">
          <stop offset="0" stop-color="#b07a1e"/>
          <stop offset="0.5" stop-color="#f3dc9a"/>
          <stop offset="1" stop-color="#b07a1e"/>
        </linearGradient>
      </defs>
      <path d="M0 505 C 150 460, 280 380, 360 210 L 360 216 C 282 386, 152 470, 0 512 Z" fill="url(#gold-cat)"/>
    </svg>
    <div class="brand">
      <div class="brand__name">Tolvern</div>
      <div class="brand__tier">FEEDS</div>
      <div class="brand__rule"></div>
    </div>
    <div class="flavor-icon" role="img" aria-label="Cow silhouette"></div>
    <div class="flavor-name">BEEF</div>
    <div class="title">
      <div class="title__freeze">Freeze</div>
      <div class="title__raw">DRIED RAW</div>
    </div>
    <div class="species">CAT<br>FOOD</div>
  </section>

</main>
</body>
</html>
```